Automotive Parts Company Business Card/Logo Design

We need a logo/business card for a new automotive parts and accessories company which is based in Barbados. The company will only have an online presence and this will reduce our overheads and allow us to pass potential savings to our customers.

We will offer most automotive parts which include, but are not limited to, accessories, exterior, interior, body parts.

We want to appeal to a very wide audience and we're looking for a modern, clean and bold design to make the company seem very professional. Our logo and facebook page will be our only customer facing items. So it is essential that these are done correctly.

The design should really communicate that we can provide premium car parts at affordable prices for all types of cars e.g. European and Japanese.

We will stock items and also source hard to get and unique pieces. We aim to not just be another shop that sells parts. But we want to work with our customers to achieve their car goals.

The company name is GearNest and our slogan is Quality Parts At Affordable Prices.
The design should be very modern, clean and bold.

I've included examples of some of the business cards I like as well as images of car products.
Updates

Dear Designers,

I've uploaded some samples of some business card/logo designs I like. Please have a look at the project brief. Just to reiterate, I am looking for a clean, modern design.

Thanks,

Rohan

Dear Designers,

Please note the Apr 14th deadline is soon approaching.

Also note the business card is double-sided.

I look forward to working with you.

Thanks,

Rohan

Target Market(s)

20 - 30 (young professionals, younger generation with disposible income) and then then all other markets

Industry/Entity Type

Automotive

Contact Information for Business Card

Rohan Mehtabrooke
GearNest
Quality Parts At Affordable Prices
https://www.example-social.test/gearnestbb
246-555-0192
gearnestbb@mailbox-demo.test

```html
<!DOCTYPE html>
<html lang="en">
<head>
<meta charset="utf-8">
<title>GearNest Business Card</title>
<link rel="stylesheet" href="https://fonts.googleapis.com/css2?family=Ubuntu:wght@400;700&display=swap">
<style>
  :root {
    --stage: #3a3a3c;
    --card-top: #2a2a2c;
    --card-bottom: #1c1c1e;
    --band: #161617;
    --rule: #3b3b3e;
    --gold: #e0a83a;
    --silver: #d9d9dc;
    --text: #f2f2f2;
  }
  * { box-sizing: border-box; margin: 0; padding: 0; }
  html, body { width: 1200px; height: 800px; overflow: hidden; }
  body {
    background: var(--stage);
    font-family: "Ubuntu", sans-serif;
    position: relative;
  }
  .card {
    position: absolute;
    top: 257px;
    width: 500px;
    height: 286px;
    border-radius: 4px;
    background: linear-gradient(160deg, var(--card-top), var(--card-bottom));
    box-shadow: 0 10px 30px rgba(0,0,0,0.45);
    overflow: hidden;
  }
  .card--front { left: 70px; }
  .card--back { left: 630px; }

  .brand { display: flex; flex-direction: column; }
  .brand__name {
    font-weight: 700;
    color: var(--gold);
    line-height: 1;
    display: flex;
    align-items: center;
    gap: 10px;
  }
  .brand__mark {
    width: 14px; height: 14px;
    border-radius: 50%;
    background: var(--gold);
  }
  .brand__slogan {
    color: var(--gold);
    font-weight: 400;
    margin-top: 6px;
  }

  .card--front .brand {
    position: absolute;
    left: 0; right: 0; top: 50%;
    transform: translateY(-50%);
    align-items: center;
  }
  .card--front .brand__name { font-size: 54px; }
  .card--front .brand__slogan { font-size: 12px; letter-spacing: 0.3px; }

  .card--back .band {
    position: absolute;
    left: 0; right: 0; top: 118px; bottom: 0;
    background: var(--band);
    border-top: 1px solid var(--rule);
  }
  .card--back .brand {
    position: absolute;
    right: 28px; top: 38px;
    align-items: flex-end;
  }
  .card--back .brand__name { font-size: 36px; }
  .card--back .brand__mark { width: 10px; height: 10px; }
  .card--back .brand__slogan { font-size: 9px; margin-top: 4px; }

  .contact {
    position: absolute;
    right: 28px; bottom: 40px;
    list-style: none;
    text-align: right;
    color: var(--text);
    font-size: 14px;
    line-height: 1.55;
  }
  .contact__label { color: var(--gold); margin-right: 4px; }
  .contact__domain { color: var(--gold); }
</style>
</head>
<body>
  <section class="card card--front" aria-label="Business card front">
    <div class="brand">
      <div class="brand__name"><span class="brand__mark"></span>GearNest</div>
      <div class="brand__slogan">Quality Parts At Affordable Prices</div>
    </div>
  </section>

  <section class="card card--back" aria-label="Business card back">
    <div class="band"></div>
    <div class="brand">
      <div class="brand__name"><span class="brand__mark"></span>GearNest</div>
      <div class="brand__slogan">Quality Parts At Affordable Prices</div>
    </div>
    <ul class="contact">
      <li><span class="contact__label">P :</span>246-555-0192</li>
      <li><span class="contact__label">E :</span>gearnestbb@mailbox-demo.test</li>
      <li><span class="contact__domain">www.example-social.test/</span>gearnestbb</li>
    </ul>
  </section>
</body>
</html>
```